Simple menu needed for Asian food truck

We are an Asian food truck that attends big festivals. Our menu is very simple featuring only about 5 or 6 dishes, but we need big pictures and lettering to capture the attention of festival goers. Our motto is "Fresh, Authentic, Homemade", it would be great to include that somewhere. We also need a menu that possibly magnetic so that we can easily take off items that are sold out, change pricing or add different dishes for specific venues. Attached is an example of what our current menu looks like.

```html
<!DOCTYPE html>
<html lang="en">
<head>
<meta charset="utf-8">
<title>Mira's Egg Rolls – Menu</title>
<link href="https://fonts.googleapis.com/css2?family=Montserrat:ital,wght@0,800;0,900;1,800&family=Big+Shoulders+Stencil+Display:wght@800&display=swap" rel="stylesheet">
<style>
  :root {
    --red: #bd1622;
    --gold: #f5cf67;
    --orange: #d97a12;
    --flame: #e8901e;
    --ink: #111;
    --motto: #f7cd55;
  }
  html, body { margin: 0; padding: 0; overflow: hidden; background: var(--red); }
  .menu {
    position: relative; width: 918px; height: 1200px; overflow: hidden;
    background: var(--red); font-family: "Montserrat", sans-serif; color: var(--ink);
  }
  .brand {
    position: absolute; left: 22px; top: 40px; width: 160px; height: 112px;
    display: flex; flex-direction: column; align-items: center; justify-content: center; gap: 8px;
  }
  .brand-dot { width: 22px; height: 22px; border-radius: 50%; background: var(--orange); }
  .brand-name {
    font-weight: 900; color: var(--orange); font-size: 24px; line-height: 1.05; text-align: center;
  }
  .motto-bar { position: absolute; left: 210px; width: 660px; height: 12px; background: var(--orange); }
  .motto-bar.top { top: 50px; }
  .motto-bar.bottom { top: 134px; }
  .motto {
    position: absolute; left: 210px; top: 66px; width: 660px; text-align: center;
    font-family: "Big Shoulders Stencil Display", sans-serif; font-weight: 800;
    font-size: 54px; line-height: 64px; color: var(--motto); white-space: nowrap;
  }
  .item { position: absolute; left: 0; width: 918px; height: 130px; }
  .photo-frame {
    position: absolute; left: 43px; top: 0; width: 186px; height: 129px; box-sizing: border-box;
    border: 3px solid var(--gold); border-radius: 14px; padding: 4px; background: var(--red);
  }
  .photo { width: 100%; height: 100%; border-radius: 10px; }
  .price {
    position: absolute; left: 264px; top: 21px; width: 99px; height: 87px; background: var(--gold);
    font-weight: 900; font-size: 56px; display: flex; align-items: center; justify-content: center;
  }
  .name {
    position: absolute; left: 385px; top: 21px; width: 493px; height: 87px; background: var(--gold);
    box-sizing: border-box; padding: 0 3px; font-weight: 800; font-size: 36px; line-height: 45px;
    display: flex; flex-direction: column; justify-content: center; white-space: nowrap;
  }
  .name.single { padding-left: 18px; font-size: 36px; }
  .name .sub { font-size: 31px; }
  .name.tall { height: 108px; justify-content: flex-start; padding-top: 2px; }
  .name .note { font-style: italic; font-size: 17px; line-height: 18px; margin-left: 3px; }
  .divider { position: absolute; left: 549px; width: 164px; height: 40px; }
  .flame { position: absolute; bottom: 0; width: 194px; height: 272px; }
  .flame.left { left: 0; }
  .flame.right { right: 0; transform: scaleX(-1); }
  .phone {
    position: absolute; left: 0; width: 918px; top: 1138px; text-align: center;
    font-weight: 900; font-size: 51px; color: var(--gold); line-height: 60px;
  }
</style>
</head>
<body>
<div class="menu">
  <svg class="flame left" viewBox="0 0 194 272" role="img" aria-label="Decorative flame flourish">
    <path d="M14 0 C2 70 4 160 16 215 C40 250 120 258 194 272 L150 272 C90 262 30 252 8 230 C-4 170 0 80 14 0 Z" fill="var(--flame)"/>
  </svg>
  <svg class="flame right" viewBox="0 0 194 272" role="img" aria-label="Decorative flame flourish">
    <path d="M14 0 C2 70 4 160 16 215 C40 250 120 258 194 272 L150 272 C90 262 30 252 8 230 C-4 170 0 80 14 0 Z" fill="var(--flame)"/>
  </svg>

  <div class="brand">
    <span class="brand-dot"></span>
    <span class="brand-name">Mira's<br>Egg Rolls</span>
  </div>

  <div class="motto-bar top"></div>
  <div class="motto">FRESH, AUTHENTIC, HOMEMADE</div>
  <div class="motto-bar bottom"></div>

  <div class="item" style="top:196px">
    <div class="photo-frame"><div class="photo" role="img" aria-label="Fried chicken egg rolls with dipping sauce" style="background:linear-gradient(135deg,#4a5a78,#c98a45 45%,#e8e4dc)"></div></div>
    <div class="price">$6</div>
    <div class="name single">Chicken Eggrolls - 3pc</div>
  </div>
  <svg class="divider" style="top:317px" role="img" aria-label="Decorative ornament"><rect x="0" y="8" width="164" height="24" rx="12" fill="var(--gold)"/></svg>

  <div class="item" style="top:355px">
    <div class="photo-frame"><div class="photo" role="img" aria-label="Fresh shrimp spring rolls with lettuce" style="background:linear-gradient(135deg,#7a9a5a,#f0e4dc 45%,#f2b8a0)"></div></div>
    <div class="price">$6</div>
    <div class="name"><span>Fresh Springrolls</span><span>(Shrimp or Veggie) - 2pc</span></div>
  </div>
  <svg class="divider" style="top:479px" role="img" aria-label="Decorative ornament"><rect x="0" y="8" width="164" height="24" rx="12" fill="var(--gold)"/></svg>

  <div class="item" style="top:515px">
    <div class="photo-frame"><div class="photo" role="img" aria-label="Glazed barbecue pork skewers" style="background:linear-gradient(135deg,#8a2a22,#5a1a14 55%,#a83a2a)"></div></div>
    <div class="price">$6</div>
    <div class="name"><span>Chinese BBQ Pork</span><span>Skewers - 2pc</span></div>
  </div>
  <svg class="divider" style="top:638px" role="img" aria-label="Decorative ornament"><rect x="0" y="8" width="164" height="24" rx="12" fill="var(--gold)"/></svg>

  <div class="item" style="top:674px">
    <div class="photo-frame"><div class="photo" role="img" aria-label="Bowl of fried rice with chopsticks" style="background:linear-gradient(135deg,#c8c0a8,#e0cc98 50%,#c87838)"></div></div>
    <div class="price">$5</div>
    <div class="name"><span>Fried Rice</span><span>(Chicken or Pork) - Bowl</span></div>
  </div>
  <svg class="divider" style="top:797px" role="img" aria-label="Decorative ornament"><rect x="0" y="8" width="164" height="24" rx="12" fill="var(--gold)"/></svg>

  <div class="item" style="top:833px">
    <div class="photo-frame"><div class="photo" role="img" aria-label="Stuffed chicken wings with salad on a plate" style="background:linear-gradient(135deg,#e07a30,#d8c8b0 50%,#b06a38)"></div></div>
    <div class="price">$8</div>
    <div class="name tall"><span>Angel Wing (Stuffed</span><span>Chicken Wing) - Combo</span><span class="note">With side of fried rice</span></div>
  </div>
  <svg class="divider" style="top:965px" role="img" aria-label="Decorative ornament"><rect x="0" y="8" width="164" height="24" rx="12" fill="var(--gold)"/></svg>

  <div class="item" style="top:1005px">
    <div class="photo-frame"><div class="photo" role="img" aria-label="Glasses of iced flavored tea" style="background:linear-gradient(135deg,#d89a40,#a0202a 45%,#e8c060)"></div></div>
    <div class="price">$5</div>
    <div class="name"><span>Flavored Tea</span><span class="sub">Strawberry, Mango or Peach</span></div>
  </div>

  <div class="phone">+1 555-014-0192</div>
</div>
</body>
</html>
```